price list for web and print- sending to inquiring clients and use as promo material

Hello
I need a graphic design for my photography price list/s. I am a people photographer. The first of 6 price sheets will be for head shots- I would like a price sheet that captures the prospective clients' attention. The info and visual should be compelling and easy to digest. It should be simple yet interesting. I will provide you with some pictures but you do not have to include them. I have a studio indoors and outdoors also working on location. This design should be for email and print. The picture of "denise" is me and I use that on all my profiles. I like the fonts in the logo but it is too boxy and rigid

Target Market(s)

repeat client, word of mouth referrals, new people but aquaintances of others that might know me

Industry/Entity Type

Graphic Design

Font styles to use
Serif
Sans Serif
Script

Requirements
Must have
• prices and maybe some words about my services that I sent in... Please tie it together as best as possible..
Nice to have
• Loosen up my logo.. it is in a box.....contemporary design but not something that would not fit in with corporate.. I like this headline
• "Create a great first impression with your professional headshots"
• I sent in other copy and my logo(sent in the picture drop box)

```html
<!DOCTYPE html>
<html lang="en">
<head>
<meta charset="utf-8">
<title>Denise M Harlow Photography – Headshot Packages</title>
<link rel="stylesheet" href="https://fonts.googleapis.com/css2?family=EB+Garamond:ital,wght@0,400;0,500;1,400&family=Oswald:wght@400;600&family=PT+Sans+Narrow:wght@700&display=swap">
<style>
  :root{
    --slate:#555555;
    --ink:#000000;
    --paper:#ffffff;
    --gold:#c8963e;
    --rule:#d6d6d6;
    --photo-sky:#5b7fa8;
    --photo-city:#a59d8f;
  }
  *{margin:0;padding:0;box-sizing:border-box}
  html,body{width:927px;height:1200px;overflow:hidden;background:var(--slate)}
  .sheet{position:relative;width:927px;height:1200px;background:var(--slate);color:var(--paper);font-family:"EB Garamond",Georgia,serif}

  .headline{position:absolute;left:43px;top:36px;width:440px;font-family:"PT Sans Narrow",Arial,sans-serif;font-weight:700;font-size:33px;line-height:42px;letter-spacing:2.6px;white-space:nowrap}

  .packages-title{position:absolute;left:43px;top:194px;font-size:36px;letter-spacing:2px;font-weight:400;line-height:1}
  .packages-intro{position:absolute;left:43px;top:231px;width:380px;font-size:17px;line-height:29px}

  .package{position:absolute;left:43px;width:396px}
  .package-head{border-top:1.5px solid var(--rule);border-bottom:1.5px solid var(--rule);height:32px;display:flex;align-items:center;white-space:nowrap}
  .package-name{font-family:"Oswald",Arial,sans-serif;font-weight:600;font-size:15px;letter-spacing:7.4px}
  .package-tag{font-style:italic;font-size:15.5px;letter-spacing:3px;margin-left:2px}
  .features{list-style:none;margin-top:4px;font-size:16px;line-height:20px}
  .features li{padding-left:21px;position:relative}
  .features li::before{content:"»";position:absolute;left:0}
  .price{text-align:right;font-family:"PT Sans Narrow",Arial,sans-serif;font-weight:700;font-size:21px;letter-spacing:1.5px;line-height:22px;margin-top:-3px}
  .extra{text-align:right;font-size:16px;line-height:20px}
  .note{width:385px;font-size:16px;line-height:19px}
  .rates{font-size:16px;line-height:19px;border-collapse:collapse}
  .rates td{padding:0;line-height:19px}
  .rates td:first-child{width:109px}

  .brand-column{position:absolute;left:491px;top:0;width:391px;height:1085px;background:var(--ink)}
  .brand-name{position:absolute;top:33px;width:100%;text-align:center;font-size:26px;font-weight:400;line-height:34px;color:var(--paper)}
  .portrait{position:absolute;top:103px;left:0;width:391px;height:574px;background:linear-gradient(180deg,var(--photo-sky) 0%,#8ea7c2 45%,var(--photo-city) 70%,#7f776b 100%)}
  .portrait-label{position:absolute;top:344px;right:11px;font-family:"Oswald",Arial,sans-serif;font-size:9.5px;letter-spacing:-.2px}

  .point{position:absolute;left:0;width:100%;text-align:center}
  .point h3{font-family:"Oswald",Arial,sans-serif;font-weight:600;font-size:15px;letter-spacing:6.5px;color:var(--gold);line-height:20px}
  .point p{margin:10px auto 0;width:352px;font-size:16.5px;line-height:21.5px}

  .contact{position:absolute;top:1122px;left:0;width:100%;text-align:center}
  .contact h2{font-family:"Oswald",Arial,sans-serif;font-weight:400;font-size:17px;letter-spacing:8px;line-height:22px}
  .contact p{font-size:18px;line-height:24px}
</style>
</head>
<body>
<main class="sheet">
  <h1 class="headline">Create a great first<br>impression with your<br>professional headshots</h1>

  <h2 class="packages-title">POPULAR PACKAGES</h2>
  <p class="packages-intro">Headshots and business portraits at my studio or at your location</p>

  <section class="package" style="top:301px">
    <div class="package-head"><span class="package-name">ENTRY PACKAGE</span><span class="package-tag">Quick and Simple</span></div>
    <ul class="features"><li>one pose</li><li>one wardrobe</li><li>one selected image retouched</li></ul>
    <p class="price">just $175</p>
    <p class="extra">Additional images just $75 each</p>
  </section>

  <section class="package" style="top:469px">
    <div class="package-head"><span class="package-name">2 POSE PACKAGE</span><span class="package-tag">Most Popular</span></div>
    <ul class="features"><li>two poses</li><li>Two wardrobe changes</li><li>Two selected images retouched</li><li>One or two background changes</li></ul>
    <p class="price">just $295</p>
    <p class="extra">Additional images just $75 each</p>
  </section>

  <section class="package" style="top:654px">
    <div class="package-head"><span class="package-name">PREMIER PACKAGE</span><span class="package-tag">Get it all</span></div>
    <ul class="features"><li>four poses</li><li>3-4 wardrobe changes</li><li>4 selected images retouched</li><li>2-3 background changes</li><li>Additional images just $75 each</li><li>optional outdoor studio</li></ul>
    <p class="price">just $525</p>
    <p class="extra">Additional images just $75 each</p>
  </section>

  <section class="package" style="top:880px">
    <div class="package-head"><span class="package-name">AT YOUR LOCATION</span><span class="package-tag">Personal branding</span></div>
    <ul class="features"><li>$250 set up charge, minimum of 5 people</li><li>one selected image retouched</li></ul>
    <p class="note">If possible, we like ½ hour appts for each person so they can view their images on the computer</p>
    <table class="rates">
      <tr><td>5-10 people</td><td>$150 each</td></tr>
      <tr><td>11-20 people</td><td>$100 each</td></tr>
      <tr><td>20 + people</td><td>$&nbsp;&nbsp;75 each</td></tr>
    </table>
    <p class="extra" style="margin-top:20px">Additional images just $50 each</p>
  </section>

  <aside class="brand-column">
    <div class="brand-name">Denise M Harlow Photography</div>
    <div class="portrait" role="img" aria-label="Business portrait of Denise in a dark blazer, arms crossed, with a city skyline behind">
      <span class="portrait-label">SAMPLE OF DENISE´S WORK</span>
    </div>

    <div class="point" style="top:708px">
      <h3>EXPERIENCE</h3>
      <p>Denise is an accomplished professional photographer who has helped thousands of clients. She is an expert at helping you look confident and approachable.</p>
    </div>
    <div class="point" style="top:832px">
      <h3>24 HOUR TURNAROUND</h3>
      <p>Your time is valuable. Denise can complete the photoshoot in just 30 miutes. (Or as long as you want.)&nbsp; Our process is designed to save your time.</p>
    </div>
    <div class="point" style="top:955px">
      <h3>ENJOYABLE</h3>
      <p>You can look forward to an enjoyable photo session with Denise´s professional guidance. Denise helps make the experiance fun.</p>
    </div>
  </aside>

  <footer class="contact">
    <h2>CONTACT DENISE TO SCHEDULE</h2>
    <p>Riverton GA 30999 • 555-014-2290 • dmhphoto@examplemail.com • http://dmhphoto.com</p>
  </footer>
</main>
</body>
</html>
```